BUSINESS CONSULTING

Would like a page design that would reflect "flow" effect that denotes moving around obstacles and logo webpage for BREXA Consulting. We provide business consulting in the areas of training/facilitation, Leadership Coaching and Development, Process Improvement and Employee On-boarding and Authorization.

Need skeletal designed to be populated at a later date.

```html
<!DOCTYPE html>
<html lang="en">
<head>
<meta charset="utf-8">
<title>BREXA Consulting</title>
<link href="https://fonts.googleapis.com/css2?family=Arimo:ital,wght@0,400;0,700;1,400&family=Open+Sans:wght@400;600&display=swap" rel="stylesheet">
<style>
:root{
  --page:#ececec;
  --panel:#ffffff;
  --teal:#1f7a87;
  --teal-dark:#176570;
  --green:#3d9a40;
  --ink:#222222;
  --muted:#666666;
  --quote:#8a8a8a;
  --link:#d62a00;
  --accent:#3aa6d8;
  --rule:#cfcfcf;
}
*{margin:0;padding:0;box-sizing:border-box}
html,body{width:1200px;height:1085px;overflow:hidden}
body{background:var(--page);font-family:Arimo,Arial,sans-serif;color:var(--ink);position:relative}
.abs{position:absolute}
.brand-mark{left:180px;top:9px;width:92px;height:92px;border:3px solid var(--teal);border-radius:50%}
.brand-name{left:284px;top:36px;font-size:31px;font-weight:700;color:var(--teal);letter-spacing:-.3px;line-height:1;white-space:nowrap}
.follow{left:675px;top:53px;font-size:9.5px;color:#333;white-space:nowrap}
.social{top:51px;width:14px;height:14px;background:#9aa7ad;border-radius:2px}
.divider{left:864px;top:46px;width:1px;height:27px;background:#cccccc}
.support{left:878px;top:45px;font-size:9.5px;color:#333;white-space:nowrap}
.phone{left:878px;top:61px;font-size:9.5px;font-weight:700;color:var(--accent)}
.nav{left:180px;top:110px;width:840px;height:43px;background:var(--teal)}
.nav-home{left:9px;top:7px;width:63px;height:29px;background:var(--green);border:1px solid #2f7d32;color:#fff;font-size:8.6px;font-weight:700;text-align:center;line-height:27px}
.nav-item{top:17px;color:#fff;font-size:8.6px;font-weight:700;letter-spacing:0;white-space:nowrap}
.search{left:618px;top:7px;width:178px;height:27px;background:#fff;font-size:11px;color:#555;padding:8px 9px}
.search-btn{left:796px;top:7px;width:29px;height:27px;background:var(--green)}
.panel{left:180px;top:153px;width:840px;height:647px;background:var(--panel)}
.slide{left:189px;top:160px;width:822px;height:343px;background:linear-gradient(180deg,#f6f6f6 0%,#d9d6d0 55%,#b9b5ad 100%)}
.arrow{top:309px;width:42px;height:41px;background:#a9a9a9;border-radius:2px}
.caption{left:393px;top:379px;width:414px;height:88px;background:rgba(70,70,70,.72);border-radius:6px;text-align:center;color:#fff;font-family:"Open Sans",sans-serif}
.caption h1{font-size:38px;font-weight:400;margin-top:4px;letter-spacing:-1px;line-height:44px}
.caption p{font-size:12.5px;color:#e6e6e6;line-height:17px}
.quote{left:221px;top:526px;width:760px;font-size:15.5px;font-style:italic;color:var(--quote);line-height:18px}
.quote-btn{left:802px;top:550px;width:166px;height:32px;background:linear-gradient(#2b95a3,var(--teal-dark));border-radius:6px;color:#fff;font-family:"Open Sans",sans-serif;font-size:12px;text-align:center;line-height:32px;box-shadow:0 2px 3px rgba(0,0,0,.3)}
.col-title{top:634px;font-size:12px;font-weight:700;letter-spacing:.3px;white-space:nowrap}
.col-icon{top:667px;width:44px;height:58px;border-radius:4px}
.col-text{top:668px;width:165px;font-size:9.5px;line-height:17px;color:#444}
.col-text b{color:#222}
.more{color:var(--link)}
.top-btn{left:964px;top:786px;width:44px;height:44px;border-radius:50%;background:#1d5c78;border:2px solid #d7e3e8;color:#fff;font-size:11px;text-align:center;padding-top:14px;box-shadow:0 2px 4px rgba(0,0,0,.3)}
.sec-title{top:825px;font-size:12px;font-weight:700;letter-spacing:.3px}
.sec-sub{top:844px;font-size:9.5px;color:var(--muted)}
.rule{height:1px;background:var(--rule)}
.welcome-photo{left:209px;top:882px;width:183px;height:82px;border:1px solid #bbb;padding:3px;background:#fff}
.welcome-photo div{width:100%;height:100%;background:linear-gradient(135deg,#e8edf0,#5b6470 70%,#2b2f36)}
.welcome-text{left:417px;top:877px;width:290px;font-size:9.5px;line-height:17px;color:#444}
.news-meta{font-size:9.5px;color:var(--accent)}
.news-meta b{font-weight:700}
.news-title{font-size:9.5px;font-weight:700;margin-top:6px}
.news-body{font-size:9.5px;color:#444;margin-top:7px}
.news-body.more{color:var(--link)}
.footer{left:0;top:1042px;width:1200px;height:43px;background:var(--teal);color:#fff;font-size:9.5px}
</style>
</head>
<body>
<header>
  <div class="abs brand-mark"></div>
  <div class="abs brand-name">BREXA Consulting</div>
  <div class="abs follow">Follow us on social network</div>
  <div class="abs social" style="left:801px"></div>
  <div class="abs social" style="left:818px"></div>
  <div class="abs social" style="left:835px"></div>
  <div class="abs divider"></div>
  <div class="abs support">Click here to live Support &nbsp;Toll Free</div>
  <div class="abs phone">1-800-555-0142</div>
</header>

<nav class="abs nav">
  <div class="abs nav-home">HOME</div>
  <div class="abs nav-item" style="left:81px">TRAINING/FACILITATION</div>
  <div class="abs nav-item" style="left:209px">LEADERSHIP COACHING &amp; DEVELOPMENT</div>
  <div class="abs nav-item" style="left:411px">PROCESS IMPROVEMENT</div>
  <div class="abs nav-item" style="left:540px">CONTACT US</div>
  <div class="abs search">Search:</div>
  <div class="abs search-btn">
    <svg width="29" height="27" viewBox="0 0 29 27"><circle cx="13" cy="12" r="5" fill="none" stroke="#fff" stroke-width="2"/><line x1="17" y1="16" x2="21" y2="20" stroke="#fff" stroke-width="2.5"/></svg>
  </div>
</nav>

<main>
  <div class="abs panel"></div>
  <div class="abs slide" role="img" aria-label="Photo of a smiling team of five business professionals"></div>
  <div class="abs arrow" style="left:205px"><svg width="42" height="41"><polyline points="24,14 18,20.5 24,27" fill="none" stroke="#fff" stroke-width="2"/></svg></div>
  <div class="abs arrow" style="left:955px"><svg width="42" height="41"><polyline points="18,14 24,20.5 18,27" fill="none" stroke="#fff" stroke-width="2"/></svg></div>
  <div class="abs caption">
    <h1>BREXA Consulting</h1>
    <p>We provide business consulting in the areas of<br>training/facilitation, Leadership Coaching and Development, Process</p>
  </div>

  <p class="abs quote">“We provide business consulting in the areas of training/facilitation, Leadership Coaching and Development, Process Improvement and Employee On-boarding and Authorization”</p>
  <div class="abs quote-btn">Click here for a free quote</div>

  <h2 class="abs col-title" style="left:210px">TRAINING/FACILITATION</h2>
  <div class="abs col-icon" style="left:210px;top:680px;height:34px;background:#9a5a2a" role="img" aria-label="Briefcase icon"></div>
  <p class="abs col-text" style="left:273px"><b>Fusce vehicula dignissim ligula.</b><br>Vestibulum sit amet neque eu neque suscipit consequat quis vel risus. Vestibulum vehicula purus nec dui<br><span class="more">continue reading »</span></p>

  <h2 class="abs col-title" style="left:489px">LEADERSHIP COACHING &amp; DEVELOPMENT</h2>
  <div class="abs col-icon" style="left:489px;width:52px;background:linear-gradient(90deg,#c8282a,#e8b83a,#3a8ad0)" role="img" aria-label="Chart with magnifier icon"></div>
  <p class="abs col-text" style="left:551px"><b>Vestibulum sit amet neque</b><br>eu neque suscipit consequat quis vel risus. Vestibulum vehicula purus nec dui accumsan fermentum.<br><span class="more">continue reading »</span></p>

  <h2 class="abs col-title" style="left:765px">EMPLOYEE ON-BOARDING</h2>
  <div class="abs col-icon" style="left:765px;width:52px;background:linear-gradient(135deg,#eef3f8,#8fb0cc)" role="img" aria-label="Clipboard checklist icon"></div>
  <p class="abs col-text" style="left:827px;width:170px"><b>Aliquam erat volutpat.</b> Curabitur blandit odio eget odio eleifend vel mattis augue convallis. Praesent fringilla, eros et tristique tempus, libero metus porttitor velit, at ultrices eros dolor placerat<br><span class="more">continue reading »</span></p>

  <div class="abs top-btn">TOP</div>

  <h2 class="abs sec-title" style="left:209px">WELCOME TO BREXA CONSULTING</h2>
  <p class="abs sec-sub" style="left:209px">Lorem ipsum dolor sit amet, consectetur adipisicing elit, sed do eiusmod tempor</p>
  <div class="abs rule" style="left:209px;top:866px;width:495px"></div>
  <div class="abs welcome-photo"><div role="img" aria-label="Photo of a business team meeting around a laptop"></div></div>
  <p class="abs welcome-text">Sed ut perspiciatis unde omnis iste natus error sit voluptatem accusantium mque laudantium, totam rem aperiam, eaque ipsa quae ab illo inventore veritatis et quasi architecto beatae vitae dicta sunt explicabo ullamco laboris nisi ut aliquip ex ea commodo consequat.<br><span class="more">read more »</span></p>

  <h2 class="abs sec-title" style="left:768px">NEWS AND EVENTS</h2>
  <p class="abs sec-sub" style="left:768px">Lorem ipsum dolor sit amet, consectetur</p>
  <div class="abs rule" style="left:768px;top:866px;width:232px"></div>
  <article class="abs" style="left:768px;top:878px;width:232px">
    <p class="news-meta">12 Dec 2013 | <b>0 comments</b></p>
    <p class="news-title">DUIS NEC PORTTITOR LOREM</p>
    <p class="news-body">Integer lacus ante then ante ullamcorper ut vulputate..</p>
  </article>
  <div class="abs rule" style="left:768px;top:935px;width:232px"></div>
  <article class="abs" style="left:768px;top:947px;width:232px">
    <p class="news-meta">18 Dec 2013 | <b>5 comments</b></p>
    <p class="news-title">AENEAN INTERDUM</p>
    <p class="news-body">Vestibulum ante ipsum luctus ultrices antene posuere.</p>
    <p class="news-body more" style="margin-top:6px">more news »</p>
  </article>
</main>

<footer class="abs footer">
  <p class="abs" style="left:180px;top:12px;white-space:nowrap">© 2014 Copyright BREXA Consulting . All Rights Reserved</p>
  <p class="abs" style="left:180px;top:24px;white-space:nowrap">Home | Contact | Privacy Policy</p>
</footer>
</body>
</html>
```